Company Pop-Up Banner Needed for Trade Shows and Events

We are a commercial waterproofing and restoration company - meaning we work on the exterior of high-rise buildings. We need a pop-up banner that incorporates our two divisions (KVR and TruMark) in one streamlined banner. We wold like it to show both catch phrases. We don't want any colors outside of our logo colors (navy blue, island blue, kelly green). I've included a few pictures if you would like to use them or your own.
Target Market(s)
Property managers, building engineers
Industry/Entity Type
It Company
Requirements
Must have
- KVR logo, TruMark logo, tag lines for each (KVR: Protecting and Enhancing your Property Investment) (TruMark: Fast Service, Quick Repairs, Customers Satisfaction - That's the TruMark Guarantee)
Nice to have
- cool pictures, interesting designs, eye catching colors
Should not have
- colors outside of logos

```html
<!DOCTYPE html>
<html lang="en">
<head>
<meta charset="utf-8">
<title>KVR &amp; TruMark Pop-Up Banners</title>
<link href="https://fonts.googleapis.com/css2?family=Open+Sans:wght@400;600;700;800&display=swap" rel="stylesheet">
<style>
  :root {
    --navy: #0d2a5e;
    --navy-deep: #0a1f47;
    --island-blue: #1ea6de;
    --kelly-green: #5bb947;
    --swoosh-grey: #8b909a;
    --paper: #ffffff;
    --stage: #e9ebee;
  }
  * { margin: 0; padding: 0; box-sizing: border-box; }
  html, body {
    width: 960px; height: 1200px; overflow: hidden;
    background: var(--stage);
    font-family: "Open Sans", Arial, sans-serif;
  }
  .banner {
    position: absolute; top: 62px;
    width: 322px; height: 1074px;
    overflow: hidden;
    box-shadow: 0 6px 18px rgba(0,0,0,.25);
  }
  .banner--kvr { left: 106px; --accent: var(--island-blue); }
  .banner--trumark { left: 512px; --accent: var(--kelly-green); }
  .banner__shapes { position: absolute; inset: 0; }

  .brand {
    position: absolute; top: 34px; left: 0; width: 100%;
    text-align: center; color: var(--navy);
  }
  .brand__name {
    display: inline-flex; align-items: center; gap: 10px;
    font-weight: 800; font-size: 60px; line-height: 1; letter-spacing: -1px;
  }
  .brand__mark {
    width: 18px; height: 18px; background: var(--accent); display: inline-block;
  }
  .brand__tag {
    margin-top: 8px; font-size: 12.5px; font-weight: 400; letter-spacing: .2px;
  }
  .banner--trumark .brand__name { font-size: 52px; }
  .banner--trumark .brand__tag { color: var(--kelly-green); letter-spacing: 1.4px; font-size: 13.5px; }

  .headline {
    position: absolute; left: 0; width: 100%;
    text-align: center; color: var(--paper);
    font-weight: 700; text-transform: uppercase;
  }
  .banner--kvr .headline { top: 236px; font-size: 31px; line-height: 45px; }
  .headline__soft { font-weight: 400; }
  .banner--trumark .headline { top: 238px; font-size: 30px; line-height: 41px; }

  .photo {
    position: absolute; border-radius: 50%;
    border: 5px solid var(--accent);
    background: linear-gradient(150deg, #8a6a58 0%, #3d5a4a 45%, #5a8f5a 70%, #2e3d52 100%);
  }
  .photo--b { background: linear-gradient(160deg, #4e5a66 0%, #7d8a94 40%, #3a6fa8 75%, #2a3442 100%); }
  .photo--c { background: linear-gradient(170deg, #7fa06a 0%, #a9b4b8 40%, #4a8a4e 65%, #3b4a3a 100%); }

  .contact {
    position: absolute; left: 0; top: 904px; width: 100%;
    text-align: center;
  }
  .contact__cta { color: var(--paper); font-weight: 600; font-size: 31px; line-height: 34px; }
  .contact__phone { color: var(--paper); font-weight: 700; font-size: 38px; line-height: 44px; }
  .contact__web { color: var(--navy); font-weight: 700; font-size: 25px; line-height: 30px; margin-top: 16px; }
</style>
</head>
<body>

<section class="banner banner--kvr">
  <svg class="banner__shapes" width="322" height="1074" viewBox="0 0 322 1074">
    <defs>
      <linearGradient id="kvr-sky" x1="0" y1="0" x2="0.3" y2="1">
        <stop offset="0" stop-color="#2a3a5e"/>
        <stop offset="1" stop-color="#0f1a33"/>
      </linearGradient>
    </defs>
    <rect width="322" height="1074" fill="url(#kvr-sky)" role="img" aria-label="Photo of a glass high-rise tower seen from below"/>
    <path d="M0 0H322V170C250 200 160 205 100 196 60 190 25 182 0 172Z" fill="#ffffff"/>
    <path d="M0 172C60 200 150 214 230 202 270 196 300 186 322 175V188C290 204 250 214 200 218 120 222 50 206 0 186Z" fill="var(--swoosh-grey)"/>
    <path d="M20 200C100 222 200 226 322 180V188C210 236 110 232 20 200Z" fill="var(--island-blue)"/>
    <path d="M0 846C80 872 200 870 322 808V822C200 884 80 886 0 862Z" fill="var(--swoosh-grey)"/>
    <path d="M0 868C90 890 210 880 322 826V1074H0Z" fill="var(--island-blue)"/>
    <path d="M0 864C90 886 210 876 322 822V830C210 884 90 894 0 872Z" fill="#ffffff"/>
  </svg>

  <div class="brand">
    <div class="brand__name">KVR<span class="brand__mark"></span></div>
    <div class="brand__tag">WATERPROOFING · RESTORATION</div>
  </div>

  <h1 class="headline">Protecting<br><span class="headline__soft">and</span><br>Enhancing<br>Your Property<br>Investment</h1>

  <div class="photo photo--a" style="left:22px;top:482px;width:176px;height:176px" role="img" aria-label="Crew on a green boom lift working on a brick building"></div>
  <div class="photo photo--b" style="left:154px;top:522px;width:146px;height:146px" role="img" aria-label="Worker in hi-vis on a lift at a glass facade"></div>
  <div class="photo photo--c" style="left:68px;top:626px;width:226px;height:226px" role="img" aria-label="Boom lift crew restoring a mirrored glass building"></div>

  <div class="contact">
    <div class="contact__cta">CALL NOW</div>
    <div class="contact__phone">0123 456 789</div>
    <div class="contact__web">WWW.WEBSITE.COM</div>
  </div>
</section>

<section class="banner banner--trumark">
  <svg class="banner__shapes" width="322" height="1074" viewBox="0 0 322 1074">
    <defs>
      <linearGradient id="tm-sky" x1="0" y1="0" x2="0.3" y2="1">
        <stop offset="0" stop-color="#0f2a63"/>
        <stop offset="1" stop-color="#0a1d45"/>
      </linearGradient>
    </defs>
    <rect width="322" height="1074" fill="url(#tm-sky)" role="img" aria-label="Photo of a modern office tower facade"/>
    <path d="M0 0H322V170C250 200 160 205 100 196 60 190 25 182 0 172Z" fill="#ffffff"/>
    <path d="M0 172C60 200 150 214 230 202 270 196 300 186 322 175V188C290 204 250 214 200 218 120 222 50 206 0 186Z" fill="var(--swoosh-grey)"/>
    <path d="M20 200C100 222 200 226 322 180V188C210 236 110 232 20 200Z" fill="var(--kelly-green)"/>
    <path d="M0 846C80 872 200 870 322 808V822C200 884 80 886 0 862Z" fill="var(--swoosh-grey)"/>
    <path d="M0 868C90 890 210 880 322 826V1074H0Z" fill="var(--kelly-green)"/>
    <path d="M0 864C90 886 210 876 322 822V830C210 884 90 894 0 872Z" fill="#ffffff"/>
  </svg>

  <div class="brand">
    <div class="brand__name"><span class="brand__mark"></span>TruMark</div>
    <div class="brand__tag">THE KVR SIGNATURE SERVICE</div>
  </div>

  <h2 class="headline">Fast Service,<br>Quick Repairs,<br>Customers<br>Satisfaction -<br>That's the<br>TruMark<br>Guarantee</h2>

  <div class="photo photo--c" style="left:36px;top:530px;width:160px;height:160px" role="img" aria-label="Boom lift crew restoring a mirrored glass building"></div>
  <div class="photo photo--b" style="left:166px;top:586px;width:136px;height:136px" role="img" aria-label="Worker in hi-vis on a lift at a glass facade"></div>
  <div class="photo photo--a" style="left:54px;top:652px;width:204px;height:204px" role="img" aria-label="Crew on a green boom lift working on a brick building"></div>

  <div class="contact">
    <div class="contact__cta">CALL NOW</div>
    <div class="contact__phone">0123 456 789</div>
    <div class="contact__web">WWW.WEBSITE.COM</div>
  </div>
</section>

</body>
</html>
```